nutrition company business card

I would like to have a business card that has two sides, one being the green color from the Company name on the logo. I am open to ideas and looks that work with my logo. I like the idea of having a negative image of the tree on the green side.

For my information on the card I must have:
Linda Moorcombe
415-872-6041
lindamoorcombe@quellmail.net

This area will need to be updated once I complete my schooling.

Reason: I need to extend my deadline by one day as I have been sick the last week and not had time to review all the new designs. Thank you.

Industry/Entity Type

Nutrition

Requirements
Must have
• I would like to have a business card that has two sides, one being the green color from the Company name on the logo. I am open to ideas and looks that work with my logo. I like the idea of having a negative image of the tree on the green side.
• For my information on the card I must have:
• Linda Moorcombe
• 415-872-6041
• lindamoorcombe@quellmail.net
• This area will need to be updated once I complete my schooling.

```html
<!DOCTYPE html>
<html lang="en">
<head>
<meta charset="utf-8">
<title>Rooted Kitchens – Business Card</title>
<link rel="stylesheet" href="https://fonts.googleapis.com/css2?family=Quicksand:wght@400;500&family=Arimo:wght@400&display=swap">
<style>
  :root {
    --backdrop: #e9e6e3;
    --green: #86c440;
    --green-light: #9ad15a;
    --taupe: #9b8a84;
    --taupe-deep: #8f7d77;
    --tag-taupe: #8e7f7a;
    --white: #ffffff;
    --card-shadow: 0 10px 24px rgba(60, 45, 35, 0.22);
  }
  * { box-sizing: border-box; margin: 0; padding: 0; }
  html, body {
    width: 1200px;
    height: 646px;
    overflow: hidden;
    background: var(--backdrop);
  }
  .canvas {
    position: relative;
    width: 1200px;
    height: 646px;
    display: flex;
    align-items: center;
    justify-content: center;
    gap: 44px;
  }
  .card {
    position: relative;
    width: 540px;
    height: 309px;
    overflow: hidden;
    box-shadow: var(--card-shadow);
  }
  .card-decor {
    position: absolute;
    inset: 0;
    width: 100%;
    height: 100%;
  }

  /* Front */
  .card-front {
    background: radial-gradient(circle at 60% 40%, var(--green-light), var(--green) 70%);
  }
  .brand {
    position: absolute;
    left: 72px;
    top: 118px;
    display: flex;
    flex-direction: column;
    align-items: flex-start;
  }
  .brand-mark {
    width: 62px;
    height: 62px;
    border-radius: 50%;
    border: 3px solid var(--tag-taupe);
    background: var(--white);
    margin: 0 0 10px 68px;
  }
  .brand-name {
    font-family: "Quicksand", sans-serif;
    font-weight: 400;
    font-size: 33px;
    line-height: 1;
    color: var(--white);
    letter-spacing: 0.5px;
  }
  .brand-tagline {
    font-family: "Quicksand", sans-serif;
    font-weight: 400;
    font-size: 23px;
    line-height: 1.05;
    color: var(--tag-taupe);
    letter-spacing: 0.6px;
  }

  /* Back */
  .card-back {
    background: linear-gradient(160deg, var(--taupe), var(--taupe-deep));
  }
  .contact-head {
    position: absolute;
    right: 30px;
    top: 96px;
    text-align: right;
  }
  .contact-name {
    font-family: "Arimo", sans-serif;
    font-size: 17px;
    color: var(--green);
    letter-spacing: 6px;
  }
  .contact-role {
    margin-top: 4px;
    font-family: "Arimo", sans-serif;
    font-size: 10px;
    color: var(--white);
    letter-spacing: 5px;
  }
  .contact-details {
    position: absolute;
    right: 30px;
    bottom: 46px;
    text-align: right;
    font-family: "Arimo", sans-serif;
    font-size: 10.5px;
    line-height: 1.7;
    color: var(--white);
  }
  .contact-details .label {
    color: var(--green);
    margin-right: 3px;
  }
  .contact-details .item + .item {
    margin-left: 10px;
  }
</style>
</head>
<body>
<main class="canvas">

  <section class="card card-front" aria-label="Card front">
    <svg class="card-decor" viewBox="0 0 540 309" aria-hidden="true">
      <circle cx="400" cy="70" r="150" fill="none" stroke="#6fa636" stroke-opacity="0.35" stroke-width="12"/>
    </svg>
    <div class="brand">
      <span class="brand-mark" aria-hidden="true"></span>
      <span class="brand-name">Rooted Kitchens</span>
      <span class="brand-tagline">healthy eating made easy</span>
    </div>
  </section>

  <section class="card card-back" aria-label="Card back">
    <svg class="card-decor" viewBox="0 0 540 309" aria-hidden="true">
      <circle cx="150" cy="225" r="165" fill="none" stroke="#7e6e69" stroke-opacity="0.45" stroke-width="12"/>
    </svg>
    <div class="contact-head">
      <p class="contact-name">Linda Moorcombe</p>
      <p class="contact-role">DESIGNATION</p>
    </div>
    <div class="contact-details">
      <p><span class="item"><span class="label">address</span>123 Your Address # Country St. 91205</span></p>
      <p>
        <span class="item"><span class="label">phone</span>415-872-6041</span>
        <span class="item"><span class="label">email</span>lindamoorcombe@quellmail.net</span>
        <span class="item"><span class="label">website</span>www.yourweb.com</span>
      </p>
    </div>
  </section>

</main>
</body>
</html>
```